Website re-design wedding music business

I need my wordpress wedding music website redesigned. I'm a wedding pianist and also provide duo/trio entertainment with other musicians and looking for an overhaul of my wordpress site.

Website: tomaslevett.com.au

Target Market(s)

brides; engaged couples

Industry/Entity Type

Wedding

Number of Pages Required

5+ page

Colors

Designer to choose colors to be used in the design.

Requirements
Must have
• I'm looking to overhaul my website which is looking rather tired after 4 years. It is functional but not inviting to visitors. Initially my website started out as a solo piano player providing music for wedding. It is gradually growing now where brides can book
• 1) Solo Piano
• 2) Duo (any combination of Piano / Cello / Vocalist / Violin)
• 3) Trio (any combination of Piano/ Cello /Vocalist / Violin)
• in future it may increase to 4 / 5 /6 piece bands so that needs to be taken into account for the future growth where I'll recruit other musicians.
• Some other functionality I'd like to see
• - Visitors want a calendar to know availability of musicians
• - Automatically providing enquiry price & discount (if applicable)
• - Automating the booking form process (manual) - There's a PDF form I send to the customer after we go back/forth on email on songs/price etc but if more of it could be automated online that would be great. If move to online it would be good to be able to override the set prices with a custom price and also providing a payment gateway
• More Flexibility on pricing - customer selects type of artists they want and it calculates a price based on who they have chosen whether it is a ceremony or canapes or reception (or combination of any). Extra transport fee is added if >50km out of Melbourne.
• How would you re-design this website. Imagine you are a bride/groom looking to book wedding music services. I would love to see some concepts .
• Please indicate any other fees required for your submission and level of support post this competition. I would like this to be an on-going relationship.
Nice to have
• I'd preferably like the website to be in wordpress as I've been familiar with it over time and can do basic updates in the back end. Happy for other suggestions if you can convince me I should move away from wordpress.

```html
<!DOCTYPE html>
<html lang="en">
<head>
<meta charset="utf-8">
<title>Tomas Levett – Wedding Pianist</title>
<link href="https://fonts.googleapis.com/css2?family=Work+Sans:wght@400;500;600;700;800&family=Lora:ital,wght@1,400;1,700&display=swap" rel="stylesheet">
<style>
:root{
  --gold:#c19d67;
  --ink:#2b2b2b;
  --muted:#6a6a6a;
  --white:#ffffff;
  --about-bg:#f4f4f4;
  --blush:#f4e4e4;
  --dark:#353535;
  --orange:#e8792c;
}
*{box-sizing:border-box;margin:0;padding:0}
html,body{width:914px;height:1200px;overflow:hidden}
body{font-family:"Work Sans",sans-serif;color:var(--ink);background:var(--white);position:relative}
.site-header{height:59px;display:flex;align-items:center;justify-content:space-between;padding:0 166px 0 168px;background:var(--white)}
.brand{display:flex;align-items:center;gap:6px;font-size:15px;letter-spacing:-.2px}
.brand-dot{width:40px;height:40px;border-radius:50%;background:#111}
.brand b{font-weight:800}
.main-nav{display:flex;gap:21px;font-size:11px;font-weight:500}
.hero{position:relative;height:394px;overflow:hidden}
.hero-photo{position:absolute;inset:0;background:radial-gradient(ellipse at 25% 40%,#6b6a55 0%,#3d4535 40%,#2a2f24 75%),#333}
.hero-photo::after{content:"";position:absolute;left:230px;right:120px;bottom:0;height:140px;background:linear-gradient(#d8d8d4,#a9aaa4);opacity:.75;border-radius:12px 12px 0 0}
.hero-copy{position:absolute;left:257px;width:400px;top:120px;text-align:center;color:var(--white)}
.hero-title{font-size:41px;font-weight:800;color:var(--gold);letter-spacing:.5px;line-height:1}
.hero-sub{font-size:10.5px;font-weight:700;margin-top:6px}
.hero-text{font-size:8.8px;line-height:15px;margin-top:12px}
.btn-book{display:inline-block;margin-top:14px;background:var(--gold);color:var(--white);font-weight:700;font-size:10px;padding:6px 13px;border-radius:2px}
.about{background:var(--about-bg);height:168px;text-align:center;padding-top:22px}
.section-title{font-size:17.5px;font-weight:800;color:var(--gold);letter-spacing:.3px}
.about p{font-size:10.5px;line-height:15px;color:var(--muted);margin:12px auto 0}
.btn-outline{display:inline-block;margin-top:20px;border:1.5px solid #444;font-size:8.5px;font-weight:700;padding:4px 17px;color:#333}
.mid{background:var(--blush);height:331px;position:relative}
.music{position:absolute;left:195px;top:22px;width:238px;text-align:center}
.player{margin-top:14px;background:#f7f7f7;box-shadow:0 0 3px rgba(0,0,0,.2);text-align:left;height:244px;position:relative;overflow:hidden}
.player-head{font-size:7.5px;font-weight:600;color:#888;padding:4px 6px;border-bottom:1px solid #e4e4e4;margin:0 2px}
.player-head span{color:var(--gold)}
.now{display:flex;padding:4px 6px;gap:6px;height:66px}
.cover{width:61px;height:61px;background:linear-gradient(135deg,#8a1e1e,#2a1818)}
.now-info{flex:1;font-size:8px;line-height:10px}
.now-info small{display:block;color:var(--gold);font-size:6.5px;font-weight:600;margin-top:7px}
.controls{display:flex;align-items:center;gap:10px;font-size:5.5px;color:#999;margin-top:7px}
.progress{height:1.5px;background:#ddd;margin-top:5px;position:relative;width:105px}
.progress i{position:absolute;left:0;top:0;height:100%;width:62%;background:var(--gold)}
.tracks{list-style:none;font-size:6.5px;letter-spacing:.3px;padding:2px 10px 0 24px}
.tracks li{display:flex;height:20px;align-items:center;position:relative}
.tracks .n{width:14px}
.tracks .t{flex:1}
.tracks .d{color:#aaa;width:34px}
.tracks .cur::before{content:"";position:absolute;left:-14px;border-left:4px solid var(--orange);border-top:3px solid transparent;border-bottom:3px solid transparent}
.player-foot{position:absolute;left:0;right:0;bottom:0;height:22px;background:var(--white);font-size:5.5px;color:#999;display:flex;align-items:center;justify-content:space-between;padding:0 8px;border-top:1px solid #eee}
.divider{position:absolute;left:458px;top:68px;width:1px;height:228px;background:#ccbcbc}
.events{position:absolute;left:488px;top:22px;width:260px}
.events .section-title{text-align:center}
.event-list{list-style:none;margin-top:15px}
.event{display:flex;gap:13px;height:47px}
.date{width:31px;height:31px;flex:none;border:1.5px solid var(--muted);color:var(--gold);font-weight:800;font-size:11px;line-height:13px;padding-left:2px;background:#f6eaea}
.event h3{font-size:12px;font-weight:600}
.event p{font-size:9px;color:var(--muted);margin-top:2px}
.btn-more{display:block;width:64px;margin:0 auto 0 84px;background:#4a4a4a;color:var(--white);font-size:7.5px;font-weight:700;text-align:center;padding:5px 0}
.testimonials{background:var(--dark);height:188px;text-align:center;padding-top:20px;position:relative;color:#d5d5d5}
.quote{font-family:"Lora",serif;font-style:italic;font-size:8.4px;line-height:15.5px;width:640px;margin:14px auto 0}
.mark{position:absolute;top:62px;font-family:"Lora",serif;font-size:46px;color:#9a9a9a;font-style:normal}
.rule{width:104px;height:1px;background:#999;margin:10px auto 0}
.author{font-family:"Lora",serif;font-style:italic;font-size:8.5px;margin-top:9px;color:#bbb}
.author b{font-size:12px;color:#ddd}
.dots{display:flex;gap:7px;justify-content:center;margin-top:17px}
.dots i{width:7px;height:7px;border-radius:50%;background:#777}
.dots i:first-child{background:var(--gold)}
.site-footer{background:var(--blush);height:60px;display:flex;align-items:center;justify-content:space-between;padding:0 166px 0 168px}
.copyright{font-size:11.5px;font-weight:600;color:#444}
.social{display:flex;gap:6px}
.social span{width:29px;height:29px;background:#444;color:var(--white);font-size:4.6px;font-weight:600;display:flex;align-items:center;justify-content:center}
</style>
</head>
<body>
<header class="site-header">
  <div class="brand"><span class="brand-dot"></span><span>TOMAS<b>LEVETT</b></span></div>
  <nav class="main-nav"><span>Home</span><span>About</span><span>Event</span><span>Prices</span><span>Gallery</span><span>Contact</span></nav>
</header>

<section class="hero">
  <div class="hero-photo" role="img" aria-label="Pianist in a dark suit playing a white grand piano under trees in a park"></div>
  <div class="hero-copy">
    <h1 class="hero-title">TOMAS LEVETT</h1>
    <p class="hero-sub">WEDDING PIANIST | EVENT PIANIST</p>
    <p class="hero-text">Tomas Levett is Melbourne's premier award wedding &amp; event<br>pianist specialising in playing beautiful background music<br>for weddings, special occasions &amp; corporate events.</p>
    <span class="btn-book">BOOK NOW</span>
  </div>
</section>

<section class="about">
  <h2 class="section-title">ABOUT</h2>
  <p>Tomas Levett is a Melbourne professional pianist with over 5 years experience<br>within the wedding industry and has played piano for<br>more than 30 years.</p>
  <span class="btn-outline">FULL BIO</span>
</section>

<section class="mid">
  <div class="music">
    <h2 class="section-title">MUSIC</h2>
    <div class="player">
      <div class="player-head"><span>Tomas Levett</span> Piano</div>
      <div class="now">
        <div class="cover" role="img" aria-label="Album cover artwork"></div>
        <div class="now-info">UNDER THE WILLOW<br>TREE<small>Film Classics</small>
          <div class="controls"><span>1:50</span>
            <svg width="10" height="7" viewBox="0 0 10 7"><path d="M0 0h1.5v7H0zM5 0v7L1.5 3.5zM9.5 0v7L6 3.5z" fill="#222"/></svg>
            <svg width="7" height="8" viewBox="0 0 7 8"><path d="M1 0h2v8H1zM4.5 0h2v8h-2z" fill="#222"/></svg>
            <svg width="10" height="7" viewBox="0 0 10 7"><path d="M0 0v7l3.5-3.5zM4.5 0v7L8 3.5zM8.5 0H10v7H8.5z" fill="#222"/></svg>
            <span>2:00</span></div>
          <div class="progress"><i></i></div>
        </div>
      </div>
      <ol class="tracks">
        <li><span class="n">1</span><span class="t">YOU'LL STAY IN MY MIND</span><span class="d">5:24</span></li>
        <li><span class="n">2</span><span class="t">WALK THE SHORELINE</span><span class="d">7:30</span></li>
        <li class="cur"><span class="n">3</span><span class="t">WHEN THE SUN ROSE</span><span class="d">4:03</span></li>
        <li><span class="n">4</span><span class="t">SO NEAR</span><span class="d">7:36</span></li>
        <li><span class="n">5</span><span class="t">I FOLLOW THE STARS</span><span class="d">7:36</span></li>
        <li><span class="n">6</span><span class="t">I Was Mistaken</span><span class="d">4:47</span></li>
        <li><span class="n">7</span><span class="t">THE MEADOW</span><span class="d">4:36</span></li>
      </ol>
      <div class="player-foot"><span>View your library →</span>
        <svg width="22" height="8" viewBox="0 0 22 8"><path d="M0 1h2l4 6h2M0 7h2l4-6h2M14 2h6v3M20 6h-6V3" stroke="#e8792c" fill="none" stroke-width="1"/></svg></div>
    </div>
  </div>
  <div class="divider"></div>
  <div class="events">
    <h2 class="section-title">UPCOMING EVENTS</h2>
    <ul class="event-list">
      <li class="event"><div class="date">30<br>JUL</div><div><h3>Private event – Seaholme (tbc)</h3><p>July 30 @ 2:00 pm - 3:00 pm</p></div></li>
      <li class="event"><div class="date">17<br>AUG</div><div><h3>Wedding Ceremony &amp; Canapes</h3><p>August 17 @ 3:30 pm - 6:00 pm</p></div></li>
      <li class="event"><div class="date">20<br>AUG</div><div><h3>Corporate event Harbourline Hotel</h3><p>August 25 @ 7:30 pm - 9:30 pm</p></div></li>
      <li class="event"><div class="date">02<br>SEP</div><div><h3>Wedding Ceremony/Canapes</h3><p>September 2 @ 8:00 am - 5:00 pm</p></div></li>
      <li class="event"><div class="date">02<br>SEP</div><div><h3>Corporate event</h3><p>September 2 @ 8:00 am - 5:00 pm</p></div></li>
    </ul>
    <span class="btn-more">VIEW MORE</span>
  </div>
</section>

<section class="testimonials">
  <h2 class="section-title">TESTIMONIALS</h2>
  <span class="mark" style="left:110px">“</span>
  <span class="mark" style="right:110px">”</span>
  <p class="quote">Tomas and Sofia (Celloist) played at our ceremony on 5th Nov 2016. They worked really well together and the music that they played was perfect. So<br>many of my guests commented that the music was so good. Tomas was really easy to work with right from the first email to the actual day.<br>We would definitely recommend them to anyone who needs a good pianist and celloist! Thanks Tomas and Sofia!</p>
  <div class="rule"></div>
  <p class="author"><b>Lena and Marco</b> - November 23 2016 - Brightwall Gallery, South Melbourne</p>
  <div class="dots"><i></i><i></i><i></i><i></i></div>
</section>

<footer class="site-footer">
  <p class="copyright">© 2017 Copyright Tomas Levett</p>
  <div class="social"><span>Friendsbook</span><span>Chirper</span><span>ViewTube</span><span>Snapgram</span><span>Pinboard</span></div>
</footer>
</body>
</html>
```